creative pack design with extended budget for Nobrelia coffee product

- we need a packing design for a new product of coffee for our company Mbelo Tiru located in Uganda.
- specialty Arabica coffee grown at slopes of Mountain Elgon with rich volcanic soils located in Eastern region of Uganda.
-  we have a logo already made and has registered in Uganda. our logo colors are mixture between a lot of brown color and yellow. vacuum  plastic bags.
- there is no restrictions towards your imagination .
-  all details available
- we will launch our product through phases ;
- phase 1 is  a ground coffee : ( Turkish coffee )  2 degrees of roasting which are ( medium dark , light ) of 250 grm
b) roasted beans: 2 degrees ( medium, dark) of 250 grm & 1000 grm
- we need also to highlight the eastern spirit of Turkish coffee
- we  need designs, the info and color only will be changed depending on previous classifications

Target Market(s)
Arab countries, Turkey , Uganda, Europe
Colors
Designer to choose colors to be used in the design.
Requirements
Nice to have
- about nature , Elgon mountain , farmers, freshness, distinctive product, soul of east such as decorated cup of Turkish coffee . these just an ideas but there is no restrictions on your imagination

```html
<!DOCTYPE html>
<html lang="en">
<head>
<meta charset="utf-8">
<title>Nobrelia Turkish Coffee – Pack Front</title>
<link rel="stylesheet" href="https://fonts.googleapis.com/css2?family=Pinyon+Script&family=Marcellus&family=Cabin:wght@400&family=Cinzel:wght@400;700&display=swap">
<style>
  :root {
    --canvas-bg: #e4e4e4;
    --amber-top: #c98f4a;
    --amber-mid: #e2a96a;
    --sand: #c7a678;
    --burlap: #a98d66;
    --espresso: #5a2c1a;
    --espresso-deep: #4a2214;
    --cream: #f6e6cc;
    --orange-type: #f0b069;
  }
  * { margin: 0; padding: 0; box-sizing: border-box; }
  html, body {
    width: 1200px; height: 900px; overflow: hidden;
    background: var(--canvas-bg);
  }
  .pack-front {
    position: absolute; left: 360px; top: 75px;
    width: 480px; height: 750px; overflow: hidden;
    background: linear-gradient(180deg, var(--amber-top) 0%, var(--amber-mid) 32%, var(--sand) 60%, var(--burlap) 100%);
    box-shadow: 0 2px 10px rgba(0,0,0,.25);
  }
  .light-stripe {
    position: absolute; left: 105px; top: 0; width: 265px; height: 300px;
    background: repeating-linear-gradient(90deg, rgba(255,240,210,.18) 0 3px, rgba(255,240,210,.06) 3px 9px);
    -webkit-mask: linear-gradient(180deg, #000 60%, transparent);
            mask: linear-gradient(180deg, #000 60%, transparent);
  }
  .scene-photo {
    position: absolute; left: 0; top: 250px; width: 480px; height: 410px;
    background:
      radial-gradient(ellipse 38% 30% at 50% 62%, rgba(235,225,205,.75), transparent 70%),
      radial-gradient(ellipse 30% 16% at 28% 66%, rgba(60,30,15,.55), transparent 70%),
      linear-gradient(180deg, rgba(140,110,80,.55) 0%, rgba(190,150,100,.35) 20%, rgba(160,125,85,.5) 55%, rgba(150,120,85,.7) 100%);
  }
  .brand-mark {
    position: absolute; left: 120px; top: 55px; width: 240px; height: 200px;
    display: flex; flex-direction: column; align-items: center; justify-content: center;
  }
  .brand-dot {
    width: 90px; height: 90px; border-radius: 50%;
    background: var(--espresso); margin-bottom: 14px;
  }
  .brand-name {
    font-family: "Cinzel", serif; font-weight: 700; font-size: 38px;
    color: var(--espresso); letter-spacing: 1px;
  }
  .product-title {
    position: absolute; left: 0; width: 100%; top: 268px; text-align: center;
    font-family: "Pinyon Script", cursive; font-size: 62px; color: var(--espresso);
  }
  .roast-badge {
    position: absolute; left: 83px; top: 360px; width: 314px; height: 62px;
  }
  .roast-badge svg { position: absolute; inset: 0; }
  .roast-badge .roast-levels {
    position: absolute; top: 9px; width: 100%; text-align: center;
    font-family: "Marcellus", serif; font-size: 21px; color: var(--cream);
  }
  .roast-badge .roast-note {
    position: absolute; top: 37px; width: 100%; text-align: center;
    font-family: "Marcellus", serif; font-size: 10px; color: var(--cream);
  }
  .format-band {
    position: absolute; left: 0; top: 658px; width: 100%; height: 47px;
    background: var(--espresso);
    display: flex; align-items: center; justify-content: center;
    font-family: "Cabin", sans-serif; font-size: 28px; color: var(--orange-type);
  }
  .net-weight {
    position: absolute; left: 0; width: 100%; top: 713px; text-align: center;
    font-family: "Marcellus", serif; font-size: 13px; color: var(--espresso-deep);
  }
</style>
</head>
<body>
  <main class="pack-front">
    <div class="light-stripe"></div>
    <div class="scene-photo" role="img" aria-label="Mountain range behind an ornate silver Turkish coffee cup and saucer on burlap with scattered roasted coffee beans"></div>

    <div class="brand-mark">
      <div class="brand-dot"></div>
      <div class="brand-name">Nobrelia</div>
    </div>

    <h1 class="product-title">Turkish Coffee</h1>

    <div class="roast-badge">
      <svg viewBox="0 0 314 62" width="314" height="62" aria-hidden="true">
        <path d="M12 0 H302 Q302 10 314 12 V50 Q302 52 302 62 H12 Q12 52 0 50 V12 Q12 10 12 0 Z" fill="#5a2c1a"/>
      </svg>
      <div class="roast-levels">MEDIUM DARK - LIGHT</div>
      <div class="roast-note">2 degrees of roasting which are</div>
    </div>

    <div class="format-band">ground coffee</div>
    <div class="net-weight">NET. 250 g</div>
  </main>
</body>
</html>
```